Alumni Ballot Postcard

We need a quick postcard to mail out to our alumni telling them that they are invited to vote on a new ballot of alumni officers. I purchased a 4 color picture I want to use for the front of the postcard from pixbarn but I can't get it to upload. Someone can email me at Marta.venn@sgfcollege-example.edu and I will email them the image. The final design needs to be clean and easy to read.

Offering doctoral, master’s, baccalaureate, and associate degrees, Saint Gideon of the Fields College is a four-year, independent Catholic institution, providing a strong foundation in the liberal arts and continuing its highly-regarded health sciences and nursing programs.

```html
<!DOCTYPE html>
<html lang="en">
<head>
<meta charset="utf-8">
<title>Alumni Ballot Postcard</title>
<link rel="stylesheet" href="https://fonts.googleapis.com/css2?family=Cinzel:wght@400;700&family=Lato:wght@400;700&family=Teko:wght@500&display=swap">
<style>
  :root {
    --navy: #0f1a44;
    --blue: #2596d1;
    --blue-light: #2ba7df;
    --blue-deep: #1a74b4;
    --white: #ffffff;
    --paper: #f4f5f7;
    --backdrop: #d9dadd;
    --ink: #1c1c1c;
    --photo-warm: #e9e1a6;
    --photo-shadow: #b7ab6e;
    --photo-cool: #3e4f8c;
  }
  * { box-sizing: border-box; margin: 0; padding: 0; }
  html, body { width: 844px; height: 1200px; overflow: hidden; }
  body { background: var(--backdrop); position: relative; font-family: "Lato", sans-serif; }

  .postcard {
    position: absolute; left: 92px; width: 675px; height: 522px;
    background: var(--white); overflow: hidden;
    box-shadow: 0 4px 14px rgba(0,0,0,.25);
  }
  .postcard--front { top: 58px; }
  .postcard--back { top: 628px; }
  .postcard__art { position: absolute; inset: 0; width: 675px; height: 522px; }

  .wordmark { position: absolute; display: flex; align-items: center; gap: 10px; }
  .wordmark__square { background: var(--ink); flex: none; }
  .wordmark__name { font-family: "Cinzel", serif; font-weight: 400; color: var(--ink); line-height: 1.05; }
  .front-wordmark { left: 420px; top: 46px; }
  .front-wordmark .wordmark__square { width: 54px; height: 54px; }
  .front-wordmark .wordmark__name { font-size: 17px; width: 170px; }
  .back-wordmark { left: 524px; top: 452px; gap: 7px; }
  .back-wordmark .wordmark__square { width: 30px; height: 30px; }
  .back-wordmark .wordmark__name { font-size: 10.5px; width: 100px; }

  .headline { font-family: "Teko", sans-serif; font-weight: 500; color: var(--blue-light); line-height: 1; white-space: nowrap; }
  .front-headline { position: absolute; left: 368px; width: 300px; top: 170px; text-align: center; font-size: 68px; }
  .tagline { position: absolute; left: 370px; width: 300px; top: 250px; text-align: center; white-space: nowrap;
    font-family: "Cinzel", serif; font-weight: 700; font-size: 17px; color: var(--ink); }
  .cta { position: absolute; left: 381px; top: 283px; width: 269px; height: 43px; background: var(--navy);
    color: var(--white); font-family: "Cinzel", serif; font-weight: 700; font-size: 25px;
    display: flex; align-items: center; justify-content: center; white-space: nowrap; }
  .front-url { position: absolute; left: 0; right: 0; top: 463px; text-align: center; white-space: nowrap;
    font-family: "Cinzel", serif; font-weight: 700; font-size: 25px; color: var(--white); letter-spacing: .5px; }

  .back-title { position: absolute; left: 50px; top: 28px; display: flex; align-items: baseline; gap: 10px; }
  .back-title__lead { font-family: "Cinzel", serif; font-weight: 700; font-size: 20px; color: var(--white); }
  .back-title .headline { font-size: 46px; color: var(--white); }

  .pill { position: absolute; height: 27px; background: var(--navy); border: 2px solid var(--white);
    border-radius: 0 14px 14px 0; color: var(--white); font-family: "Cinzel", serif; font-weight: 700;
    font-size: 15px; display: flex; align-items: center; padding-left: 24px; white-space: nowrap; }
  .pill--about { left: -4px; top: 88px; width: 126px; }
  .pill--contact { left: 103px; top: 371px; width: 136px; border-radius: 14px; padding-left: 20px; }

  .about-copy { position: absolute; left: 24px; top: 123px; width: 340px; color: var(--white);
    font-size: 14.2px; line-height: 17.6px; }
  .about-copy p + p { margin-top: 6px; }

  .back-url { position: absolute; left: 27px; top: 315px; font-family: "Cinzel", serif; font-weight: 700;
    font-size: 16px; color: var(--navy); white-space: nowrap; }

  .contact-list { position: absolute; left: 20px; top: 404px; width: 205px; list-style: none; color: var(--white); font-size: 15px; }
  .contact-list li { display: flex; align-items: center; justify-content: flex-end; gap: 8px; height: 28px; white-space: nowrap; }
  .contact-list svg { width: 15px; height: 15px; fill: var(--white); }

  .stamp-box { position: absolute; left: 585px; top: 79px; width: 66px; height: 83px; border: 1.5px solid #333; }
  .address-line { position: absolute; left: 445px; width: 206px; height: 2px; background: #333; }
  .address-line--1 { top: 335px; }
  .address-line--2 { top: 368px; }
  .address-line--3 { top: 399px; }
</style>
</head>
<body>

<section class="postcard postcard--front">
  <svg class="postcard__art" viewBox="0 0 675 522">
    <defs>
      <linearGradient id="front-photo" x1="0" y1="0" x2="1" y2="1">
        <stop offset="0" stop-color="#d8d2b8"/>
        <stop offset=".5" stop-color="var(--photo-warm)"/>
        <stop offset="1" stop-color="var(--photo-shadow)"/>
      </linearGradient>
      <linearGradient id="front-band" x1="0" y1="0" x2="1" y2="0">
        <stop offset="0" stop-color="var(--blue-deep)"/>
        <stop offset="1" stop-color="var(--blue-light)"/>
      </linearGradient>
      <linearGradient id="paper-fade" x1="0" y1="0" x2="0" y2="1">
        <stop offset="0" stop-color="#ffffff"/>
        <stop offset="1" stop-color="#e7e9ee"/>
      </linearGradient>
    </defs>
    <rect width="675" height="522" fill="url(#paper-fade)"/>
    <path role="img" aria-label="Photo of a priest in white vestments raising the host" fill="url(#front-photo)"
      d="M0,0 H305 C270,90 268,230 298,300 C318,350 250,405 0,455 Z"/>
    <path fill="var(--blue-light)" d="M305,0 H325 C285,100 280,240 312,305 C330,350 260,410 0,462 V455 C250,405 318,350 298,300 C268,230 270,90 305,0Z"/>
    <path fill="var(--navy)" d="M325,0 H398 C325,100 300,250 350,320 C400,388 550,392 675,382 V418 C500,428 300,442 0,474 V462 C260,410 330,350 312,305 C280,240 285,100 325,0Z"/>
    <path fill="none" stroke="var(--blue-light)" stroke-width="7" d="M402,0 C330,100 305,250 354,318 C404,385 552,388 675,378"/>
    <path fill="none" stroke="var(--white)" stroke-width="2.5" d="M0,466 C300,436 500,424 675,410"/>
    <path fill="url(#front-band)" d="M0,474 C300,442 500,428 675,418 V522 H0Z"/>
  </svg>
  <div class="wordmark front-wordmark">
    <span class="wordmark__square"></span>
    <span class="wordmark__name">Saint Gideon of the Fields College</span>
  </div>
  <h1 class="headline front-headline">PLEASE VOTE!</h1>
  <p class="tagline">WE VALUE YOUR OPINION</p>
  <p class="cta">VOTE TODAY!</p>
  <p class="front-url">WWW.SGFCOLLEGE-EXAMPLE.EDU</p>
</section>

<section class="postcard postcard--back">
  <svg class="postcard__art" viewBox="0 0 675 522">
    <defs>
      <linearGradient id="back-panel" x1="0" y1="0" x2="1" y2="0">
        <stop offset="0" stop-color="var(--blue-deep)"/>
        <stop offset="1" stop-color="var(--blue-light)"/>
      </linearGradient>
      <linearGradient id="back-photo" x1="0" y1="0" x2="1" y2="1">
        <stop offset="0" stop-color="#c9b9ab"/>
        <stop offset=".55" stop-color="var(--photo-cool)"/>
        <stop offset="1" stop-color="#1f2b5a"/>
      </linearGradient>
    </defs>
    <rect width="675" height="522" fill="var(--white)"/>
    <path fill="#dfe1e6" d="M472,0 H500 C480,200 420,380 290,522 H262 C390,380 455,200 472,0Z"/>
    <path fill="url(#back-panel)" d="M0,0 H440 C425,110 405,210 382,302 H0Z"/>
    <path fill="url(#back-panel)" d="M0,351 H362 C335,420 300,475 262,522 H0Z"/>
    <path fill="var(--navy)" d="M440,0 H474 C458,200 395,380 262,522 H236 C340,400 415,200 440,0Z"/>
    <circle cx="308" cy="427" r="74" fill="var(--navy)"/>
    <circle role="img" aria-label="Photo of a nursing student checking a patient's blood pressure" cx="308" cy="427" r="69" fill="url(#back-photo)"/>
  </svg>

  <div class="back-title">
    <span class="back-title__lead">ALUMNI:</span>
    <h2 class="headline">PLEASE VOTE!</h2>
  </div>

  <p class="pill pill--about">ABOUT US</p>
  <div class="about-copy">
    <p>Over the past year and a half, the Alumni Association Executive Committee has been working on a major revision to the Alumni Association bylaws. The goal is a stronger and more inclusive Alumni Association.</p>
    <p>In order to confirm the new bylaws we need alumni approval.&nbsp; Go to sgfcollege-example.edu/alumni-feedback to give us your responses to the proposed bylaws and to vote on a new slate of officers.</p>
  </div>

  <p class="back-url">WWW.SGFCOLLEGE-EXAMPLE.EDU</p>

  <p class="pill pill--contact">CONTUCT US</p>
  <ul class="contact-list">
    <li>Fairhaven, LA 70000
      <svg viewBox="0 0 16 16"><path d="M8 1 L1 7.5 H3 V15 H6.5 V10.5 H9.5 V15 H13 V7.5 H15Z"/></svg>
    </li>
    <li>(555) 014-2700
      <svg viewBox="0 0 16 16"><path d="M3.6 1.2 L6 3.6 L4.6 5.6 C5.4 7.6 8.4 10.6 10.4 11.4 L12.4 10 L14.8 12.4 L13 14.6 C7.5 14.4 1.6 8.5 1.4 3 Z"/></svg>
    </li>
  </ul>

  <div class="stamp-box"></div>
  <div class="address-line address-line--1"></div>
  <div class="address-line address-line--2"></div>
  <div class="address-line address-line--3"></div>

  <div class="wordmark back-wordmark">
    <span class="wordmark__square"></span>
    <span class="wordmark__name">Saint Gideon of the Fields College</span>
  </div>
</section>

</body>
</html>
```